Business card for a Exhibition booth fabrication company

Hi. My company would like to change our corporate name card. We are an events and Exhibition stand builder company. We would like our corporate name card to resonate what we do. I need someone to create something unique that relates to the industry that I am in. The graphic designer should be creative to incorporate the elements of my industry and try to blend in well in the design of the card. Our aim is to ensure that we are unique and our card can look different from our competitors.
Updates

The decision maker was very busy and didnt had time to make this decision

Target Market(s)

Marketing and events manager from all companies

Contact Information for Business Card

The business card should have the following details:
Name
Job Title
Email
Website

Colors

Designer to choose colors to be used in the design.

Requirements
Must have
• The card must be look something that is relevant to the service that I am providing. My website is: www.velmora-buildworks.example
• You can see my website to get more information on what service that I am doing
Nice to have
• On the back of my card, I would like to have a globe image with the incorporation of my company logo. This is to indicate that my services can be done in any part of the world.

```html
<!DOCTYPE html>
<html lang="en">
<head>
<meta charset="UTF-8">
<title>Velmora Buildworks – Business Card</title>
<link href="https://fonts.googleapis.com/css2?family=Montserrat:wght@400;500;600&display=swap" rel="stylesheet">
<style>
  :root {
    --page-bg: #e9e7e4;
    --card-bg: #333334;
    --card-bg-light: #3b3b3c;
    --brand-red: #e8232a;
    --text-grey: #8d8d8f;
    --text-light: #d9d9d9;
    --globe-tone: #3f3f41;
  }
  * { box-sizing: border-box; margin: 0; padding: 0; }
  html, body {
    width: 1200px; height: 900px; overflow: hidden;
    background: var(--page-bg);
    font-family: "Montserrat", sans-serif;
  }
  .sheet {
    width: 1200px; height: 900px;
    display: flex; flex-direction: column;
    align-items: center; justify-content: center; gap: 44px;
  }
  .card {
    width: 660px; height: 378px;
    background: linear-gradient(160deg, var(--card-bg-light), var(--card-bg));
    position: relative; overflow: hidden;
    box-shadow: 0 6px 18px rgba(0,0,0,.25);
  }
  /* back side */
  .globe {
    position: absolute; left: 110px; top: -70px;
    width: 440px; height: 440px; border-radius: 50%;
    background: radial-gradient(circle at 40% 40%, var(--globe-tone), var(--card-bg) 72%);
  }
  .back-brand {
    position: absolute; left: 0; right: 0; top: 150px;
    text-align: center;
  }
  .back-brand .brand-name {
    color: var(--brand-red); font-weight: 600;
    font-size: 32px; letter-spacing: 6px; white-space: nowrap;
  }
  .tagline {
    margin-top: 22px; color: var(--text-light);
    font-size: 17px; font-weight: 400; white-space: nowrap;
  }
  /* front side */
  .front-brand {
    position: absolute; left: 40px; top: 150px; width: 270px;
    color: var(--brand-red); font-weight: 600;
    font-size: 26px; letter-spacing: 2px; line-height: 1.25;
    text-align: center;
  }
  .details { position: absolute; left: 340px; top: 110px; }
  .person-name {
    color: var(--text-grey); font-weight: 600; font-size: 25px; letter-spacing: .5px;
    white-space: nowrap;
  }
  .job-title {
    color: var(--brand-red); font-weight: 400; font-size: 18px;
    letter-spacing: 1px; margin-top: 2px; white-space: nowrap;
  }
  .contacts { list-style: none; margin-top: 30px; }
  .contacts li {
    display: flex; align-items: center; gap: 12px;
    color: var(--text-grey); font-size: 15px; margin-bottom: 10px;
    white-space: nowrap;
  }
  .contacts svg { width: 16px; height: 16px; flex: none; }
</style>
</head>
<body>
<main class="sheet">
  <section class="card card-back">
    <div class="globe" role="img" aria-label="Faint world globe map in dark grey"></div>
    <div class="back-brand">
      <p class="brand-name">VELMORA BUILDWORKS</p>
      <p class="tagline">Shaping Bold Ideas Into Stands</p>
    </div>
  </section>

  <section class="card card-front">
    <p class="front-brand">VELMORA<br>BUILDWORKS</p>
    <div class="details">
      <p class="person-name">YOUR NAME</p>
      <p class="job-title">JOB TITLE</p>
      <ul class="contacts">
        <li>
          <svg viewBox="0 0 16 16" aria-hidden="true"><rect x="4" y="1" width="8" height="14" rx="1.5" fill="none" stroke="#e8232a" stroke-width="1.6"/><circle cx="8" cy="12.3" r="0.9" fill="#e8232a"/></svg>
          000 000 0000
        </li>
        <li>
          <svg viewBox="0 0 16 16" aria-hidden="true"><rect x="1" y="3" width="14" height="10" fill="#e8232a"/><path d="M1 3l7 6 7-6" fill="none" stroke="#333334" stroke-width="1.2"/></svg>
          youremail@velmora.example
        </li>
        <li>
          <svg viewBox="0 0 16 16" aria-hidden="true"><g fill="none" stroke="#e8232a" stroke-width="1.3"><circle cx="8" cy="8" r="6.5"/><ellipse cx="8" cy="8" rx="3" ry="6.5"/><path d="M1.5 8h13M2.5 4.5h11M2.5 11.5h11"/></g></svg>
          www.velmora-buildworks.example
        </li>
      </ul>
    </div>
  </section>
</main>
</body>
</html>
```